Zielgruppe
Wir sind IT Dienstleister und würden gerne mal eine etwas "andere" Visitenkarte haben. Wir machen alles von Netzwerken über TK Anlagen über Infrastrukturbetreuung bis hin zum Bau von Richtfunkstrecken.
Hallo,
wir brauchen neue Visitenkarten, die alten sind einfach Out :-P Der Designer hat freie Hand! Es muss nur unser Logo mit auftauchen! Die Visitenkarten sollen beidseitig sein und folgende Informationen enthalten:
Vorname Nachname
Funktion
Anschrift
Telefon inkl. Durchwahl
ggf. Mobil
Fax
eMail
Web
Helpdesk/Ticketsystem

```html
<!DOCTYPE html>
<html lang="de">
<head>
<meta charset="utf-8">
<title>Visitenkarte KABELWERK</title>
<link href="https://fonts.googleapis.com/css2?family=Fira+Sans+Condensed:wght@300;400;600;700&display=swap" rel="stylesheet">
<style>
  :root {
    --bg: #e6e6e4;
    --card-dark: #333335;
    --card-light: #f2f2f0;
    --accent: #8cc21f;
    --text-light: #ffffff;
    --text-dark: #3a3a3c;
  }
  * { margin: 0; padding: 0; box-sizing: border-box; }
  html, body { width: 1200px; height: 920px; overflow: hidden; }
  body {
    background: var(--bg);
    font-family: "Fira Sans Condensed", Arial, sans-serif;
    display: flex;
    align-items: center;
    justify-content: center;
    gap: 40px;
  }
  .card {
    width: 540px;
    height: 349px;
    position: relative;
    overflow: hidden;
    box-shadow: 0 6px 18px rgba(0,0,0,0.18);
  }
  .card--front { background: var(--card-dark); }
  .card--back { background: var(--card-dark); }

  .brand {
    display: flex;
    align-items: center;
    gap: 10px;
    color: var(--text-light);
    font-weight: 700;
    letter-spacing: 0.04em;
  }
  .brand__mark { width: 12px; height: 12px; background: var(--accent); }
  .card--front .brand {
    position: absolute;
    left: 50%; top: 50%;
    transform: translate(-50%, -50%);
    font-size: 40px;
  }
  .card--back .brand {
    position: absolute;
    right: 34px; top: 150px;
    font-size: 24px;
  }

  .person {
    position: absolute;
    left: 0; right: 0; top: 44px;
    text-align: center;
    color: var(--text-light);
  }
  .person__name { font-size: 38px; font-weight: 400; letter-spacing: 0.02em; }
  .person__role { font-size: 16px; font-weight: 300; margin-top: 2px; }

  .contact-band {
    position: absolute;
    left: 0; right: 0; bottom: 0;
    height: 88px;
    background: var(--card-light);
    display: flex;
    justify-content: space-between;
    padding: 16px 30px;
    color: var(--text-dark);
    font-size: 14px;
    line-height: 19px;
  }
  .contact-group { display: grid; grid-template-columns: 16px auto; column-gap: 8px; align-items: center; }
  .contact-group svg { width: 13px; height: 13px; fill: var(--accent); }
</style>
</head>
<body>

  <section class="card card--front">
    <div class="brand"><span class="brand__mark"></span>KABELWERK</div>
  </section>

  <section class="card card--back">
    <div class="person">
      <div class="person__name">Jonas Beispielmann</div>
      <div class="person__role">Grafikdesigner</div>
    </div>
    <div class="brand"><span class="brand__mark"></span>KABELWERK</div>

    <div class="contact-band">
      <div class="contact-group">
        <svg viewBox="0 0 24 24" aria-hidden="true"><path d="M12 2a7 7 0 0 0-7 7c0 5 7 13 7 13s7-8 7-13a7 7 0 0 0-7-7zm0 9.5A2.5 2.5 0 1 1 12 6.5a2.5 2.5 0 0 1 0 5z"/></svg>
        <span>Beispielweg 4</span>
        <span></span>
        <span>54321 Ortsheim</span>
        <svg viewBox="0 0 24 24" aria-hidden="true"><circle cx="12" cy="12" r="10" fill="none" stroke="currentColor"/><path d="M12 2a10 10 0 1 0 0 20 10 10 0 0 0 0-20zm0 2c1.5 2 2.3 5 2.3 8s-.8 6-2.3 8c-1.5-2-2.3-5-2.3-8s.8-6 2.3-8zM4 12h16v1H4z"/></svg>
        <span>www.kabelwerk-beispiel.de</span>
      </div>
      <div class="contact-group">
        <svg viewBox="0 0 24 24" aria-hidden="true"><path d="M6.6 10.8a15 15 0 0 0 6.6 6.6l2.2-2.2c.3-.3.7-.4 1-.2 1.1.4 2.3.6 3.6.6.6 0 1 .4 1 1V20c0 .6-.4 1-1 1A17 17 0 0 1 3 4c0-.6.4-1 1-1h3.5c.6 0 1 .4 1 1 0 1.3.2 2.5.6 3.6.1.3 0 .7-.2 1z"/></svg>
        <span>0987-654-321-10</span>
        <svg viewBox="0 0 24 24" aria-hidden="true"><path d="M6 2h9l3 3v5H6zM3 11h18v10H3zm3 3v2h4v-2zm0 3v2h4v-2zm8-3v5h4v-5z"/></svg>
        <span>0987-654-321-11</span>
        <svg viewBox="0 0 24 24" aria-hidden="true"><path d="M2 5h20v14H2zm2 2v.5l8 5.5 8-5.5V7l-8 5.5z"/></svg>
        <span>info@beispielmann.de</span>
      </div>
    </div>
  </section>

</body>
</html>
```